Fairbrook's Vacation Rentals Business Card

Multi Million dollar villa rentals in the Dominican Republic.

Industry/Entity Type

Business

Contact Information for Business Card

I am looking for a high-end look around my company name/logo (see attached) on one side incorporating the following info: first and last name, title, address, phone #, email and company website. On the backside I want to add a full color picture of one of our villas (see attached).

```html
<!DOCTYPE html>
<html lang="en">
<head>
<meta charset="utf-8">
<title>Fairbrook's Vacation Rentals Business Card</title>
<link rel="stylesheet" href="https://fonts.googleapis.com/css2?family=Open+Sans:wght@400;600&display=swap">
<style>
  :root {
    --backdrop: #e4e4e2;
    --card: #ffffff;
    --ink: #2a2a2a;
    --ink-soft: #4a4a4a;
    --accent: #f0561e;
    --accent-warm: #f7931e;
    --band-dark: #1f1f1f;
    --photo-light: #ece7dd;
    --photo-blue: #7fb7df;
  }
  * { box-sizing: border-box; margin: 0; padding: 0; }
  html, body {
    width: 1200px; height: 987px; overflow: hidden;
    background: var(--backdrop);
    font-family: "Open Sans", Arial, sans-serif;
    color: var(--ink);
  }
  .card {
    position: absolute;
    left: 293px; width: 615px; height: 352px;
    background: var(--card);
    box-shadow: 0 2px 6px rgba(0,0,0,0.18);
    overflow: hidden;
  }
  .card--front { top: 130px; }
  .card--back { top: 517px; }

  .brand {
    position: absolute; right: 29px; top: 56px;
    display: flex; align-items: center; gap: 10px;
  }
  .brand__dot { width: 34px; height: 34px; border-radius: 50%; background: var(--accent-warm); flex: none; }
  .brand__name {
    font-size: 26px; font-weight: 600; line-height: 1.05; color: var(--ink);
  }

  .holder { position: absolute; left: 28px; top: 188px; right: 29px; }
  .holder__name { font-size: 22px; font-weight: 600; color: var(--accent); line-height: 1.2; }
  .holder__title { font-size: 16px; color: var(--ink); line-height: 1.3; padding-bottom: 6px; border-bottom: 1.5px solid var(--ink); }

  .contact { position: absolute; left: 28px; top: 248px; list-style: none; }
  .contact li { display: flex; align-items: center; gap: 8px; font-size: 16px; color: var(--ink-soft); height: 23.5px; }
  .contact svg { width: 14px; height: 14px; fill: var(--accent); flex: none; }

  .address {
    position: absolute; right: 29px; top: 272px; text-align: right;
    font-size: 16px; color: var(--ink-soft); line-height: 23.5px; font-style: normal;
  }

  .band { position: absolute; left: 0; right: 0; bottom: 0; height: 11px; }
  .band__dark { position: absolute; left: 0; bottom: 0; height: 11px; width: 406px; background: var(--band-dark); clip-path: polygon(0 0, 100% 0, calc(100% - 5px) 100%, 0 100%); }
  .band__accent { position: absolute; right: 0; bottom: 0; height: 11px; width: 212px; background: linear-gradient(90deg, var(--accent), var(--accent-warm)); clip-path: polygon(5px 0, 100% 0, 100% 100%, 0 100%); }

  .villa-photo {
    position: absolute; left: 80px; top: 0; right: 0; bottom: 0;
    background:
      linear-gradient(90deg, #ffffff 0%, rgba(255,255,255,0) 14%),
      linear-gradient(160deg, var(--photo-blue) 0%, var(--photo-light) 45%, var(--photo-light) 65%, var(--photo-blue) 100%);
  }
  .brand-vertical {
    position: absolute; left: 14px; top: 20px; bottom: 20px;
    display: flex; flex-direction: column-reverse; align-items: center; gap: 12px;
  }
  .brand-vertical .brand__name {
    writing-mode: vertical-rl; transform: rotate(180deg);
    font-size: 27px; text-align: center;
  }
</style>
</head>
<body>
  <section class="card card--front">
    <div class="brand">
      <span class="brand__dot"></span>
      <span class="brand__name">Fairbrook's<br>Vacation Rentals</span>
    </div>

    <div class="holder">
      <h1 class="holder__name">Daniel Hale</h1>
      <p class="holder__title">CEO/Founder</p>
    </div>

    <ul class="contact">
      <li>
        <svg viewBox="0 0 16 16" aria-hidden="true"><path d="M3.6 1.2l2.3 2.9-1.3 1.8c.9 2 2.5 3.6 4.5 4.5l1.8-1.3 2.9 2.3-1.3 2.4C7 13.4 2.6 9 1.2 3.1z"/></svg>
        555 014 2538
      </li>
      <li>
        <svg viewBox="0 0 16 16" aria-hidden="true"><path d="M1 3h14v10H1z M2.2 4.2L8 8.6l5.8-4.4z" fill-rule="evenodd"/></svg>
        stay@fairbrook.com
      </li>
      <li>
        <svg viewBox="0 0 16 16" aria-hidden="true"><circle cx="8" cy="8" r="7"/><path d="M5 4c1 1 2 1 2 2.5S5.5 8 5.5 9.5 7 11 7 13M10 3.5c-.5 1.5.5 2 1.5 2.5s1 2-.5 2.5" stroke="#fff" stroke-width="1.1" fill="none"/></svg>
        www.fairbrook.com
      </li>
    </ul>

    <address class="address">
      4120 Harbor View Lane<br>
      Sosua, Puerto Plata 57000
    </address>

    <div class="band">
      <span class="band__dark"></span>
      <span class="band__accent"></span>
    </div>
  </section>

  <section class="card card--back">
    <div class="villa-photo" role="img" aria-label="Full colour photograph of a white two-storey villa with terracotta roof, balcony, sun loungers and a pool"></div>
    <div class="brand-vertical">
      <span class="brand__dot"></span>
      <span class="brand__name">Fairbrook's<br>Vacation Rentals</span>
    </div>
  </section>
</body>
</html>
```